Up to the Challenge? Canadian based consulting company needs a two sided business card design

A Canadian based security risk management consulting company needs a two-sided business card design. What we do is provide advice and guidance related to emergency, security and business continuity management for small, medium and large companies to help ensure the protection of their people, assets, information, services, operations and reputation.

The final design should be simple, only one or two colours, eye catching, professional and one that makes people look at three or more times just because it looks so darn good.

I have include examples of business cards I like.

Target Market(s)

Small, medium and large companies.

Industry/Entity Type

Security

Contact Information for Business Card

Business Card Size: Standard size of 3.5" (89mm) x 2.0" (51mm) - (see full specifications and guides on PRINTA's website if required)
Card Stock: Looking to use PRINTA's Velda 32pt stock textured paper - seam colour either chili red or black
Business Name: The Harrowfield Group
Website: www.theharrowfieldgroup.example
Telephone: (555)214-0397
Name: Dana Forsythe
Position: Principle
e-mail: Dana.Forsythe@theharrowfieldgroup.example

Font styles to use
Serif

Colors
ec1f27
000000
9d9d9d
aaaaaa
606060

Requirements
Must have
• - "The Harrowfield Group" logo (see uploaded files). I have included grey scale and colour versions.
• - Business card details (as above)
Nice to have
• - One side black or grey scale.
• - Other side would likely be white.
• - Everyone likes the silver logo on the black background.
• - Small element of colour i.e. red but I'm leaning more to greyscale.
Should not have
• - A lot of colour. Keep it simple.

```html
<!DOCTYPE html>
<html lang="en">
<head>
<meta charset="utf-8">
<title>The Harrowfield Group — Business Card</title>
<link rel="stylesheet" href="https://fonts.googleapis.com/css2?family=Cinzel:wght@400;600&family=Cormorant+Garamond:wght@400;500&display=swap">
<style>
  :root {
    --backdrop: #e6e4e0;
    --paper: #f4f4f3;
    --ink-dark: #4a4a4a;
    --ink-mid: #606060;
    --rule: #9d9d9d;
    --band: #8c8c8c;
    --band-text: #eeeeee;
    --emblem-light: #aaaaaa;
    --emblem-dark: #8e8e8e;
    --card-black: #1d1f21;
    --silver: #9a9c9e;
  }
  * { box-sizing: border-box; margin: 0; padding: 0; }
  html, body {
    width: 1200px; height: 780px; overflow: hidden;
    background: var(--backdrop);
  }
  .canvas { position: relative; width: 1200px; height: 780px; }

  .card { position: absolute; box-shadow: 0 10px 26px rgba(0,0,0,.18); }

  /* Front side */
  .card-front {
    left: 110px; top: 70px; width: 360px; height: 630px;
    background: var(--paper);
    font-family: "Cormorant Garamond", Georgia, serif;
    color: var(--ink-dark);
    text-align: center;
    overflow: hidden;
  }
  .holder-name {
    margin-top: 46px;
    font-family: "Cinzel", "Times New Roman", serif;
    font-weight: 600; font-size: 27px; letter-spacing: 3px;
    color: var(--ink-dark);
  }
  .holder-title { font-size: 19px; color: var(--ink-mid); margin-top: -4px; }
  .contact-rule { width: 290px; height: 1px; margin: 0 auto; background: var(--rule); }
  .contact-rule.top { margin-top: 20px; }
  .contact-list { padding: 16px 0 18px; }
  .contact-label { font-size: 14px; color: var(--ink-mid); letter-spacing: .5px; }
  .contact-value { font-size: 19px; color: var(--ink-dark); margin-bottom: 8px; }
  .contact-value.email { font-size: 14.5px; letter-spacing: .2px; }
  .emblem-area {
    position: absolute; left: 50px; top: 300px; width: 260px; height: 250px;
    background: radial-gradient(ellipse at 50% 55%, var(--emblem-light), var(--paper) 72%);
    opacity: .55;
  }
  .web-band {
    position: absolute; left: 0; bottom: 0; width: 100%; height: 70px;
    background: var(--band);
    border-top: 6px solid var(--paper);
    box-shadow: 0 -2px 0 var(--band);
    display: flex; align-items: center; justify-content: center;
    font-size: 16px; letter-spacing: .5px; color: var(--band-text);
  }

  /* Back side */
  .card-back {
    left: 560px; top: 250px; width: 560px; height: 320px;
    background: var(--card-black);
    display: flex; align-items: center; justify-content: center; gap: 34px;
  }
  .brand-name {
    font-family: "Cinzel", "Times New Roman", serif;
    font-weight: 400; color: var(--silver);
    text-align: left; line-height: 1.1;
  }
  .brand-name .line-main { display: block; font-size: 34px; letter-spacing: 2px; }
  .brand-name .line-sub { display: block; font-size: 24px; letter-spacing: 9px; }
  .brand-square { width: 64px; height: 64px; background: var(--silver); }
</style>
</head>
<body>
<main class="canvas">
  <section class="card card-front">
    <h1 class="holder-name">DANA FORSYTHE</h1>
    <p class="holder-title">Principle</p>
    <div class="contact-rule top"></div>
    <div class="contact-list">
      <p class="contact-label">Phone</p>
      <p class="contact-value">(555)214-0397</p>
      <p class="contact-label">Email</p>
      <p class="contact-value email">Dana.Forsythe@theharrowfieldgroup.example</p>
    </div>
    <div class="contact-rule"></div>
    <div class="emblem-area" role="img" aria-label="Large grey company emblem decoration"></div>
    <footer class="web-band">www.theharrowfieldgroup.example</footer>
  </section>

  <section class="card card-back">
    <p class="brand-name">
      <span class="line-main">THE HARROWFIELD</span>
      <span class="line-sub">GROUP</span>
    </p>
    <div class="brand-square"></div>
  </section>
</main>
</body>
</html>
```